Re-design of current business cards

We are updating our website with new colors and layout. Would like to re-design our business cards to co-ordinate. See attached pdf with new Brindlecraft website colors. We would also like to combine our 2 brands on the one business card. Attached is the new design for our Brindlecraft website, current business cards, which are one sided, brindlecraft logo in tiff, .ai for fonts. Brindlecraft logo font is Optimum, Quillmarsh website home page image, Quillmarsh brand statics for products which includes the logo for this brand.

Quillmarsh brand will stay the dark gray on the website. See attached statics for product and website home page.
Updates

The business cards will be 2 sided. Brindlecraft Brand on one side and Quillmarsh Brand on the other. The colors for Brindlecraft need to follow the color scheme of the brindlecraft website pdf I uploaded. The colors are a blue, lighter teal blue and white. Quillmarsh needs to follow the dark gray color on files uploaded

Target Market(s)

The trade and consumers

Industry/Entity Type

Home Furnishing

Contact Information for Business Card

We are updating our website with new colors and layout. Would like to re-design our business cards to co-ordinate. We would also like to combine our 2 brands onto 1 2 sided business cards.

Requirements
Must have
• Colors that match our new website, see attached image.
• RGB colors
• navy -#152842
• teal - 98aeb9
• The gray color used for Quillmarsh brands.
• ll logos and fonts should stay the same.

```html
<!DOCTYPE html>
<html lang="en">
<head>
<meta charset="utf-8">
<title>Brindlecraft / Quillmarsh Business Card</title>
<link href="https://fonts.googleapis.com/css2?family=Marcellus&family=Roboto+Condensed:wght@400;700&family=Nanum+Gothic&display=swap" rel="stylesheet">
<style>
  :root {
    --page-bg: #ffffff;
    --card-bg: #ffffff;
    --brindle-navy: #152842;
    --brindle-teal: #98aeb9;
    --quill-gray: #58595b;
    --contact-ink: #5f6670;
    --label-ink: #2a2a2a;
  }
  html, body {
    margin: 0;
    padding: 0;
    width: 1200px;
    height: 1000px;
    overflow: hidden;
    background: var(--page-bg);
  }
  .canvas {
    position: relative;
    width: 1200px;
    height: 1000px;
  }
  .sheet-label {
    position: absolute;
    left: 932px;
    top: 62px;
    margin: 0;
    font-family: "Nanum Gothic", sans-serif;
    font-size: 16px;
    color: var(--label-ink);
  }
  .card {
    position: absolute;
    left: 372px;
    width: 456px;
    height: 295px;
    background: var(--card-bg);
    box-shadow: 0 1px 4px rgba(0,0,0,0.28);
  }
  .card--front { top: 183px; }
  .card--back  { top: 522px; }

  /* Front: Brindlecraft brand */
  .brand-brindle {
    position: absolute;
    left: 0;
    right: 0;
    top: 112px;
    text-align: center;
  }
  .brand-brindle__dot {
    display: block;
    width: 30px;
    height: 30px;
    margin: 0 auto 10px;
    border-radius: 50%;
    background: var(--brindle-teal);
  }
  .brand-brindle__name {
    display: block;
    font-family: "Marcellus", serif;
    font-size: 26px;
    letter-spacing: 0.6px;
    line-height: 1;
    color: var(--brindle-navy);
    white-space: nowrap;
  }

  /* Back: Quillmarsh brand + contact */
  .brand-quill {
    position: absolute;
    left: 212px;
    top: 62px;
    display: flex;
    align-items: center;
    gap: 10px;
  }
  .brand-quill__square {
    width: 22px;
    height: 22px;
    background: var(--quill-gray);
  }
  .brand-quill__name {
    font-family: "Marcellus", serif;
    font-size: 25px;
    line-height: 1;
    color: var(--quill-gray);
    white-space: nowrap;
  }
  .contact {
    position: absolute;
    left: 242px;
    top: 134px;
    font-family: "Roboto Condensed", sans-serif;
    color: var(--contact-ink);
  }
  .contact__name {
    margin: 0;
    font-size: 13.5px;
    font-weight: 700;
    letter-spacing: 0.3px;
    line-height: 1;
  }
  .contact__title {
    margin: 7px 0 0;
    font-size: 12.5px;
    line-height: 1;
  }
  .contact__details {
    margin: 16px 0 0;
    padding: 0;
    list-style: none;
    font-size: 8.6px;
    line-height: 13.3px;
  }
</style>
</head>
<body>
<div class="canvas">
  <p class="sheet-label">Business Card(Front/Back)</p>

  <section class="card card--front" aria-label="Card front, Brindlecraft">
    <div class="brand-brindle">
      <span class="brand-brindle__dot"></span>
      <span class="brand-brindle__name">BRINDLECRAFT</span>
    </div>
  </section>

  <section class="card card--back" aria-label="Card back, Quillmarsh">
    <div class="brand-quill">
      <span class="brand-quill__square"></span>
      <span class="brand-quill__name">QUILLMARSH</span>
    </div>
    <div class="contact">
      <p class="contact__name">DANA WHITLOW</p>
      <p class="contact__title">Graphics/Photography Director</p>
      <ul class="contact__details">
        <li>PO BOX 412/1870 Fernbrook RD</li>
        <li>Millhaven, Ohio 43210</li>
        <li>Phone: 555 201 4837</li>
        <li>Fax: 555 201 4890</li>
        <li>Email: dwhitlow@brindlecraft.com</li>
        <li>www.brindlecraft.com</li>
      </ul>
    </div>
  </section>
</div>
</body>
</html>
```